Great job! Very fast work and beautiful design! Thanks again.
Zielgruppe
Die kuvrent GmbH bietet professionelle Cloud-Lösungen im Bereich spezialisierter Verwaltungssysteme. Hierbei handelt es sich um Software as a Service (SaaS), die zu 100% von der kuvrent GmbH betrieben und kontinuierlich weiterentwickelt wird.
Aufgabenstellung
Das Design kann Farben und/oder Elemente der kuvrent GmbH enthalten (www.kuvrent.de). Da es sich um ein eigenen Produkt handelt, muss jedoch auch Neutralität bewahrt werden.

```html
<!DOCTYPE html>
<html lang="de">
<head>
<meta charset="utf-8">
<title>Webparzel – Domain Liste</title>
<link href="https://fonts.googleapis.com/css2?family=Roboto:wght@400;500;700&display=swap" rel="stylesheet">
<style>
:root{
  --red:#e31e2b;
  --navy:#3d5e8c;
  --white:#ffffff;
  --ink:#1e1e1e;
  --muted:#9a9a9a;
  --line:#d9d9d9;
  --head:#f3f3f3;
  --green:#14b886;
  --gray-bar:#a3a3a3;
  --tip:#3b3b3b;
}
*{box-sizing:border-box;margin:0;padding:0}
html,body{width:1200px;height:675px;overflow:hidden}
body{font-family:"Roboto",sans-serif;color:var(--ink);background:var(--navy);position:relative}
.abs{position:absolute}
.topbar{left:0;top:0;width:1200px;height:62.5px;background:var(--red);color:var(--white)}
.brand{left:175px;top:20px;display:flex;align-items:center;gap:7px;font-size:18px;font-weight:500;letter-spacing:.2px}
.brand-dot{width:18px;height:18px;border-radius:50%;border:2px solid var(--white)}
.topbar .meta{font-size:8.8px;display:flex;align-items:center;gap:5px}
.session-bar{left:941px;top:30.5px;width:84px;height:4px;background:var(--white);border-radius:2px;overflow:hidden}
.session-bar span{display:block;width:72%;height:100%;background:var(--green)}
.mainnav{left:0;top:62.5px;width:1200px;height:35px;background:var(--white)}
.mainnav a{position:absolute;top:12.5px;font-size:8.8px;font-weight:500;color:var(--ink);text-decoration:none}
.mainnav a.active{color:var(--red)}
.mainnav a.active::after{content:"";position:absolute;left:0;right:0;top:20.5px;height:2px;background:var(--red)}
.sidebar{left:175px;top:127.5px;width:197.5px;height:507.5px;background:var(--white);border-radius:3px}
.sidebar .item{position:absolute;left:10px;width:177.5px;height:25.6px;display:flex;align-items:center;padding-left:10px;font-size:10px;font-weight:500}
.sidebar .item.active{background:var(--red);color:var(--white);border-radius:3px}
.sidebar .item svg{position:absolute;right:-2px}
.panel{background:var(--white);border-radius:3px;overflow:hidden}
.panel-bar{position:absolute;left:0;top:0;width:100%;height:6px}
.filter{left:392.5px;top:127.5px;width:632.5px;height:224px}
.list{left:392.5px;top:371px;width:633.75px;height:264px}
.title{font-size:12.5px;font-weight:500}
.label{font-size:8.8px;font-weight:500}
.field{height:19px;border:1px solid var(--line);border-radius:3px;background:var(--white);font-size:8.5px;color:var(--muted);display:flex;align-items:center;padding:0 7px;justify-content:space-between}
.field.focus{border:1.5px solid #f0a6ab;color:var(--ink);box-shadow:0 0 0 1px #fbe1e3}
.btn{background:var(--red);color:var(--white);font-size:8.8px;font-weight:700;border-radius:3px;display:flex;align-items:center;justify-content:center}
.table{left:20px;top:82px;width:593.75px;height:129px;border:1px solid var(--line);border-radius:3px;overflow:hidden}
.thead{position:absolute;left:0;top:0;width:100%;height:30px;background:var(--head);border-bottom:1px solid var(--line)}
.row{position:absolute;left:0;width:100%;height:30px;border-bottom:1px solid var(--line)}
.row:last-child{border-bottom:none}
.cell{position:absolute;top:50%;transform:translateY(-50%);font-size:8.8px}
.check{width:9.5px;height:9.5px;border:1px solid #b5b5b5;border-radius:2px;background:var(--white)}
.check.on{background:var(--green);border-color:var(--green)}
.dots{display:flex;gap:3px}
.dots i{width:5.5px;height:5.5px;border-radius:50%;border:1px solid #cfcfcf;display:block}
.dots i.on{background:var(--green);border-color:var(--green)}
.badge{display:inline-block;margin-left:8px;font-size:5px;font-weight:700;color:var(--green);border:1px solid var(--green);border-radius:6px;padding:1px 5px;vertical-align:middle}
.icon{width:20px;height:20px;border-radius:50%;display:flex;align-items:center;justify-content:center}
.icon.hover{background:#efefef}
.tip{background:var(--tip);color:var(--white);font-size:6.8px;padding:2px 5px;border-radius:2px;white-space:nowrap;transform:translateX(-50%)}
</style>
</head>
<body>

<header class="abs topbar">
  <div class="abs brand"><span class="brand-dot"></span>Webparzel</div>
  <div class="abs meta" style="left:610px;top:14px">
    <svg width="10" height="8" viewBox="0 0 10 8"><rect width="10" height="8" rx="1" fill="#fff"/><path d="M0.5 0.8 5 4.3 9.5 0.8" stroke="#e31e2b" fill="none" stroke-width="1"/></svg>neue Nachichten</div>
  <div class="abs meta" style="left:610px;top:29px">
    <svg width="10" height="10" viewBox="0 0 10 10"><circle cx="5" cy="5" r="5" fill="#fff"/><path d="M5 2.2V5.3H7.3" stroke="#e31e2b" stroke-width="1.2" fill="none"/></svg>Aufragsstapel</div>
  <div class="abs meta" style="left:816px;top:14px">Version: 2.2.8</div>
  <div class="abs meta" style="left:879px;top:14px">Sitemap</div>
  <div class="abs meta" style="left:941px;top:14px;font-weight:700">angemeldet als marlene</div>
  <div class="abs session-bar"><span></span></div>
  <div class="abs meta" style="left:941px;top:40px;font-size:7.5px">120 min. Restzeit</div>
  <div class="abs meta" style="left:1127px;top:27px;font-weight:500">
    <svg width="10" height="10" viewBox="0 0 10 10" fill="none" stroke="#fff" stroke-width="1.1"><path d="M4 1H1V9H4"/><path d="M3.5 5H9.5M7.5 3 9.5 5 7.5 7"/></svg>Logout</div>
</header>

<nav class="abs mainnav">
  <a style="left:175px">Start</a>
  <a style="left:224px">Benutzer</a>
  <a style="left:289px">Kontakt</a>
  <a class="active" style="left:350px">Domain</a>
  <a style="left:410px">DNS</a>
</nav>

<aside class="abs sidebar">
  <div class="item active" style="top:10px">Domain Liste</div>
  <div class="item" style="top:40.5px">Domain registrieren</div>
  <div class="item" style="top:71px">Domain transferieren</div>
  <div class="item" style="top:101.5px">Domain bearbeiten</div>
  <div class="item" style="top:132px">Domain wiederherstellen</div>
  <div class="item" style="top:163px">Messenaufrage</div>
  <div class="item" style="top:193.5px">DNSSEC<svg width="8" height="5" viewBox="0 0 8 5"><path d="M1 1 4 4 7 1" stroke="#333" fill="none" stroke-width="1.2"/></svg></div>
  <div class="item" style="top:224px">Werkzeug<svg width="8" height="5" viewBox="0 0 8 5"><path d="M1 1 4 4 7 1" stroke="#333" fill="none" stroke-width="1.2"/></svg></div>
</aside>

<section class="abs panel filter">
  <div class="panel-bar" style="background:var(--red)"></div>
  <div class="abs title" style="left:20px;top:20.5px">Listen-Filter</div>
  <div class="abs label" style="left:398px;top:22.5px">Zeilen pro siete</div>
  <div class="abs field" style="left:462.5px;top:18.5px;width:54px">-<svg width="7" height="5" viewBox="0 0 8 5"><path d="M1 1 4 4 7 1" stroke="#777" fill="none" stroke-width="1.2"/></svg></div>
  <div class="abs label" style="left:528px;top:22.5px">Wreiter optionen</div>
  <svg class="abs" style="left:600px;top:23px" width="8" height="8" viewBox="0 0 8 8"><path d="M4 0V8M0 4H8" stroke="#888" stroke-width="1"/></svg>

  <div class="abs label" style="left:20px;top:60.5px">Domain*</div>
  <div class="abs field focus" style="left:112.5px;top:56.5px;width:150px">webparzel.co|</div>
  <div class="abs label" style="left:20px;top:90px">Benutzer*</div>
  <div class="abs field" style="left:112.5px;top:86px;width:150px"><span></span><svg width="7" height="5" viewBox="0 0 8 5"><path d="M1 1 4 4 7 1" stroke="#555" fill="none" stroke-width="1.2"/></svg></div>
  <div class="abs label" style="left:20px;top:119.5px">Renewal-Mode*</div>
  <div class="abs field" style="left:112.5px;top:115.5px;width:150px"><span></span><svg width="7" height="5" viewBox="0 0 8 5"><path d="M1 1 4 4 7 1" stroke="#555" fill="none" stroke-width="1.2"/></svg></div>
  <div class="abs label" style="left:20px;top:149px">Expire On*</div>
  <div class="abs field" style="left:112.5px;top:145px;width:150px">DD/MM/YYYY<svg width="9" height="9" viewBox="0 0 9 9" fill="none" stroke="#666" stroke-width="1"><rect x=".5" y="1.5" width="8" height="7" rx="1"/><path d="M.5 3.5H8.5M2.5 0V2M6.5 0V2"/></svg></div>

  <div class="abs label" style="left:371px;top:63px">Umlautdomain*</div>
  <div class="abs field" style="left:462.5px;top:58.5px;width:150px"></div>
  <div class="abs label" style="left:371px;top:91.5px">Kontakt*</div>
  <div class="abs field" style="left:462.5px;top:87px;width:150px"></div>
  <div class="abs label" style="left:371px;top:120px">Lock-Status*</div>
  <div class="abs field" style="left:462.5px;top:116px;width:150px"><span></span><svg width="7" height="5" viewBox="0 0 8 5"><path d="M1 1 4 4 7 1" stroke="#555" fill="none" stroke-width="1.2"/></svg></div>
  <div class="abs label" style="left:371px;top:149px">bis*</div>
  <div class="abs field" style="left:462.5px;top:145px;width:150px">DD/MM/YYYY<svg width="9" height="9" viewBox="0 0 9 9" fill="none" stroke="#666" stroke-width="1"><rect x=".5" y="1.5" width="8" height="7" rx="1"/><path d="M.5 3.5H8.5M2.5 0V2M6.5 0V2"/></svg></div>

  <div class="abs btn" style="left:501.5px;top:182px;width:110.5px;height:22px">Domains auflisten</div>
</section>

<section class="abs panel list">
  <div class="panel-bar" style="background:var(--gray-bar)"></div>
  <div class="abs title" style="left:20px;top:28.5px">Liste</div>
  <div class="abs label" style="right:20px;top:24px">Export CSV</div>
  <div class="abs label" style="left:20px;top:51.5px">3 Elemente</div>
  <div class="abs field" style="left:91.5px;top:46.5px;width:251px;color:var(--ink)">neuedesign-webparzel.com - tesdomain-webparzel...<svg width="7" height="5" viewBox="0 0 8 5"><path d="M1 1 4 4 7 1" stroke="#333" fill="none" stroke-width="1.2"/></svg></div>

  <div class="abs table">
    <div class="thead">
      <div class="cell label" style="left:9.5px">Status</div>
      <div class="cell label" style="left:71.5px">Domain</div>
    </div>
    <div class="row" style="top:30px">
      <div class="cell check on" style="left:10px"><svg width="8" height="8" viewBox="0 0 8 8"><path d="M1.5 4 3.3 5.8 6.5 2" stroke="#fff" fill="none" stroke-width="1.3"/></svg></div>
      <div class="cell dots" style="left:29px"><i></i><i></i><i class="on"></i></div>
      <div class="cell" style="left:71.5px">neuesdesign-webparzel.com<span class="badge">Neu!</span></div>
      <div class="cell icon hover" style="left:517px"><svg width="11" height="11" viewBox="0 0 11 11" fill="none" stroke="#333" stroke-width="1.1"><path d="M5 1.5H1.5V9.5H9.5V6"/><path d="M4 7 4.3 5.3 8.5 1.1 9.9 2.5 5.7 6.7Z"/></svg></div>
      <div class="cell icon" style="left:542px"><svg width="11" height="11" viewBox="0 0 11 11" fill="none" stroke="#999" stroke-width="1.1"><path d="M2 5.5A3.8 3.8 0 1 0 3.2 2.7"/><path d="M1.5 1.5V3.6H3.6"/><path d="M5.7 3.5V5.8L7.2 7"/></svg></div>
      <div class="cell icon" style="left:567px"><svg width="4" height="10" viewBox="0 0 4 10" fill="#999"><circle cx="2" cy="1.2" r="1.1"/><rect x="1.1" y="3.5" width="1.8" height="6"/></svg></div>
    </div>
    <div class="row" style="top:60px">
      <div class="cell check" style="left:10px"></div>
      <div class="cell dots" style="left:29px"><i></i><i></i><i class="on"></i></div>
      <div class="cell" style="left:71.5px">test-webparzel.com<span class="badge">Neu!</span></div>
      <div class="cell icon" style="left:517px"><svg width="11" height="11" viewBox="0 0 11 11" fill="none" stroke="#999" stroke-width="1.1"><path d="M5 1.5H1.5V9.5H9.5V6"/><path d="M4 7 4.3 5.3 8.5 1.1 9.9 2.5 5.7 6.7Z"/></svg></div>
      <div class="cell icon hover" style="left:542px"><svg width="11" height="11" viewBox="0 0 11 11" fill="none" stroke="#333" stroke-width="1.2"><path d="M2 5.5A3.8 3.8 0 1 0 3.2 2.7"/><path d="M1.5 1.5V3.6H3.6"/><path d="M5.7 3.5V5.8L7.2 7"/></svg></div>
      <div class="cell icon" style="left:567px"><svg width="4" height="10" viewBox="0 0 4 10" fill="#999"><circle cx="2" cy="1.2" r="1.1"/><rect x="1.1" y="3.5" width="1.8" height="6"/></svg></div>
    </div>
    <div class="row" style="top:90px">
      <div class="cell check" style="left:10px"></div>
      <div class="cell dots" style="left:29px"><i></i><i></i><i class="on"></i></div>
      <div class="cell" style="left:71.5px">testdomain-webparzel.com<span class="badge">Neu!</span></div>
      <div class="cell icon" style="left:517px"><svg width="11" height="11" viewBox="0 0 11 11" fill="none" stroke="#999" stroke-width="1.1"><path d="M5 1.5H1.5V9.5H9.5V6"/><path d="M4 7 4.3 5.3 8.5 1.1 9.9 2.5 5.7 6.7Z"/></svg></div>
      <div class="cell icon" style="left:542px"><svg width="11" height="11" viewBox="0 0 11 11" fill="none" stroke="#999" stroke-width="1.1"><path d="M2 5.5A3.8 3.8 0 1 0 3.2 2.7"/><path d="M1.5 1.5V3.6H3.6"/><path d="M5.7 3.5V5.8L7.2 7"/></svg></div>
      <div class="cell icon hover" style="left:567px"><svg width="4" height="10" viewBox="0 0 4 10" fill="#222"><circle cx="2" cy="1.2" r="1.1"/><rect x="1.1" y="3.5" width="1.8" height="6"/></svg></div>
    </div>
  </div>

  <div class="abs tip" style="left:547px;top:139px">Bearbeiten</div>
  <div class="abs tip" style="left:572px;top:169px">Historie</div>
  <div class="abs tip" style="left:597px;top:199px">Whois</div>

  <div class="abs btn" style="left:514.5px;top:222px;width:99.5px;height:22px">Massenauftrag</div>
</section>

</body>
</html>
```